Two documents one design language.

We are a small insurance broker who is committed to being open and transparent as possible with our customers.

For years, we have used plain word documents (see attachments) for our Policy Wording and our Terms of Business.

But now think we can do better and these plain documents are falling behind what our competitors are offering.

So we are now looking for both these documents to be professionally designed using the same design language for both.

We are putting few constraints on the design, but we do have some:
- It must be done in word as the wording can be changed at any time, so we must be able to maintain the documents ourselves.
- Any pictures or graphics you use must be royalty free so we can re-produce with any complications.
- Any pictures or graphics you use must been supplied as part of the package.
- You MUST NOT change any wording or grammar, it's not ours to change, its the insurers wording and HAS to be agreed with them.
- You must not split any any paragraph or bullet point over two pages.
- We are an insurance broker so what ever design you use, must look professional and inspire confidence... I.e. if you read it your thoughts turn to, these people are approachable, know what they are doing and will look after me.
- We specialise in musical instrument insurance, so we are looking for musical theming.

```html
<!DOCTYPE html>
<html lang="en">
<head>
<meta charset="utf-8">
<title>Harlow Reed Insurance – Policy Wording</title>
<link rel="stylesheet" href="https://fonts.googleapis.com/css2?family=Archivo+Black&family=Arimo:wght@400;700&display=swap">
<style>
  :root{
    --backdrop:#dcc8ca;
    --paper:#f3f2f3;
    --paper-white:#ffffff;
    --brand-pink:#e783a8;
    --rose-wash:#d99db4;
    --rose-deep:#c57e98;
    --ink-dark:#4f4f52;
    --ink-body:#5a5a5e;
    --text-on-rose:#fdf3f6;
    --stage-blue:#2b4f8f;
    --stage-amber:#d88a3a;
  }
  *{box-sizing:border-box;margin:0;padding:0}
  html,body{width:1200px;height:800px;overflow:hidden}
  body{background:var(--backdrop);font-family:"Arimo",Arial,sans-serif;position:relative}

  .page{position:absolute;top:145px;width:360px;height:510px;overflow:hidden;box-shadow:0 2px 10px rgba(80,40,50,.18)}

  /* Cover */
  .cover{left:35px;background:var(--paper)}
  .cover-texture{position:absolute;inset:0;background:radial-gradient(circle at 30% 40%,#f8f7f8 0,#eeedee 60%,#e9e8e9 100%)}
  .brand-mark{position:absolute;top:78px;left:0;right:0;text-align:center}
  .brand-name{font-family:"Arimo",Arial,sans-serif;font-weight:700;font-size:17px;letter-spacing:.5px;color:var(--ink-dark);line-height:1.15;display:flex;align-items:center;justify-content:center;gap:8px}
  .brand-dot{width:9px;height:9px;border-radius:50%;background:var(--brand-pink);display:inline-block}
  .brand-note{font-size:6.5px;color:var(--ink-body);margin-top:4px;letter-spacing:.4px}
  .cover-illustration{position:absolute;left:70px;top:150px;width:220px;height:300px;border-radius:6px;background:radial-gradient(ellipse at 50% 45%,rgba(231,131,168,.45) 0,rgba(231,131,168,.18) 55%,rgba(231,131,168,0) 80%)}

  /* Spread */
  .spread-left{left:445px;background:var(--rose-wash)}
  .spread-right{left:805px;background:var(--paper-white)}

  .stage-photo{position:absolute;left:0;top:0;width:190px;height:100%;background:linear-gradient(160deg,var(--stage-blue) 0%,#6b5a7a 35%,var(--stage-amber) 60%,#3a2a2a 100%)}
  .piano-photo{position:absolute;left:190px;top:0;width:170px;height:100%;background:linear-gradient(180deg,#dca6bb 0%,var(--rose-wash) 40%,var(--rose-deep) 100%)}
  .hall-photo{position:absolute;left:0;top:0;width:218px;height:100%;background:linear-gradient(170deg,#e3b4c5 0%,var(--rose-wash) 45%,var(--rose-deep) 100%)}

  .section-title{position:absolute;font-family:"Archivo Black","Arial Black",sans-serif;font-size:25px;line-height:1.08;text-transform:uppercase;letter-spacing:.3px}
  .amend-title{left:18px;top:42px;color:var(--brand-pink)}
  .renew-title{left:150px;top:70px;color:var(--ink-dark)}

  .body-copy{position:absolute;font-size:6.4px;line-height:1.42;text-align:justify}
  .body-copy p+p{margin-top:6px}
  .amend-copy{left:200px;top:22px;width:148px;color:var(--text-on-rose)}
  .renew-copy{left:226px;top:172px;width:124px;color:var(--ink-body)}
</style>
</head>
<body>

  <section class="page cover">
    <div class="cover-texture" role="img" aria-label="Faint pattern of musical instrument outlines"></div>
    <div class="brand-mark">
      <div class="brand-name"><span class="brand-dot"></span>HARLOW REED INSURANCE</div>
      <div class="brand-note">Established 1983</div>
    </div>
    <div class="cover-illustration" role="img" aria-label="Pink line illustration of a cherub playing a harp"></div>
  </section>

  <section class="page spread-left">
    <div class="stage-photo" role="img" aria-label="Photograph of a pianist performing on stage under blue and amber lights"></div>
    <div class="piano-photo" role="img" aria-label="Rose-tinted photograph of a grand piano"></div>
    <h2 class="section-title amend-title">How to<br>amend<br>your<br>policy</h2>
    <div class="body-copy amend-copy">
      <p>Should YOU need to amend YOUR policy, please contact Harlow Reed Insurance Services by phone, email or letter advising US of the amendments YOU need to make. Any amendment may impact the cost of YOUR policy.</p>
      <p>If there is an additional cost for the change YOU will be advised prior to confirming YOU wish to proceed. Please note: the change will not become effective until the additional cost has been received.</p>
      <p>If the change YOU make results in a return YOU will be advised before confirming the change. Please note, to comply with anti money laundering legislation WE are required to make all refunds by the same method of payment the funds were originally received. In addition WE do not give refunds if the value is below £10.</p>
    </div>
  </section>

  <section class="page spread-right">
    <div class="hall-photo" role="img" aria-label="Rose-tinted photograph of a pianist at a grand piano in a concert hall"></div>
    <h2 class="section-title renew-title">Renewing<br>your<br>policy</h2>
    <div class="body-copy renew-copy">
      <p>WE will invite YOU to renew YOUR policy with US at least 21 days prior to the end of this policy. At this time WE will send YOU a renewal package which will highlight the cost of renewal along with other crucial information about YOUR new policy.</p>
      <p>WE strongly encourage YOU to read the renewal package throughly, paying close attention to the value of the instruments and accessories as manufacturers frequently increase their prices and if YOU wish to benefit from New for Old cover, it is crucial WE are advised of any change in values to retain the benefit of New for Old cover.</p>
      <p>YOUR invitation to renew is sent by post and Email to YOUR registered address and email. It is therefore important to ensure WE have YOUR current contact details at all times.</p>
      <p>In addition WE are concious of the environmental impact of sending renewal package by post, should YOU wish, WE can mark YOUR policy as paperless, please let US know if YOU would like to take advantage of a paperless policy.</p>
    </div>
  </section>

</body>
</html>
```